I need a logo design and a business card design for a new strategy consultancy that I set up called Corvanel LLC. We help clients make strategically important decisions, cutting through the cloud of noise. The design should imply clarity, simplicity and wisdom.

```html
<!DOCTYPE html>
<html lang="en">
<head>
<meta charset="utf-8">
<title>Corvanel LLC — Business Cards</title>
<link href="https://fonts.googleapis.com/css2?family=Montserrat:wght@500&family=Roboto:wght@400;700&display=swap" rel="stylesheet">
<style>
  :root {
    --stage: #2e2e2e;
    --stage-light: #4a4a4a;
    --card-white: #ffffff;
    --card-dark: #262626;
    --accent: #1fb0d8;
    --ink: #2b2b2b;
    --ink-soft: #4a4a4a;
    --text-light: #f2f2f2;
  }
  * { margin: 0; padding: 0; box-sizing: border-box; }
  html, body { width: 1200px; height: 900px; overflow: hidden; }
  body {
    background: radial-gradient(ellipse at 50% 45%, var(--stage-light) 0%, var(--stage) 70%);
    font-family: "Roboto", Arial, sans-serif;
    position: relative;
  }
  .card {
    position: absolute;
    width: 560px;
    height: 320px;
    border-radius: 24px;
    overflow: hidden;
    background: var(--card-white);
    box-shadow: 0 14px 30px rgba(0,0,0,0.45);
  }
  .card--back { left: 320px; top: 95px; }
  .card--front { left: 320px; top: 470px; }
  .card-shape { position: absolute; inset: 0; }

  .brand {
    position: absolute;
    display: flex;
    align-items: center;
    font-family: "Montserrat", Arial, sans-serif;
    font-weight: 500;
    color: var(--accent);
    text-transform: uppercase;
    white-space: nowrap;
  }
  .brand-dot { border-radius: 50%; background: var(--accent); flex: none; }
  .card--back .brand { left: 150px; top: 70px; font-size: 26px; letter-spacing: 6px; gap: 18px; }
  .card--back .brand-dot { width: 54px; height: 54px; }
  .card--front .brand { left: 28px; top: 30px; font-size: 13px; letter-spacing: 3px; gap: 10px; }
  .card--front .brand-dot { width: 26px; height: 26px; }

  .site {
    position: absolute;
    left: 150px; top: 222px;
    font-size: 18px;
    letter-spacing: 2px;
    color: var(--text-light);
  }
  .site-name { color: var(--accent); }

  .person { position: absolute; right: 32px; top: 88px; text-align: right; }
  .person-name { font-weight: 700; font-size: 30px; color: var(--accent); letter-spacing: 0.5px; line-height: 1; }
  .person-role { font-size: 15px; color: var(--ink-soft); letter-spacing: 3px; margin-top: 6px; }

  .contacts { position: absolute; right: 24px; top: 186px; list-style: none; }
  .contact {
    display: flex; justify-content: flex-end; align-items: center; gap: 12px;
    height: 24px; font-size: 15px; color: var(--text-light);
  }
  .contact svg { width: 16px; height: 16px; flex: none; }
</style>
</head>
<body>

<section class="card card--back" aria-label="Card back">
  <svg class="card-shape" viewBox="0 0 560 320" aria-hidden="true">
    <path d="M0 150 H196 L212 174 H560 V320 H0 Z" fill="var(--card-dark)"/>
    <path d="M196 150 L212 174 H560 V168 H215 L200 145 Z" fill="var(--accent)"/>
  </svg>
  <div class="brand"><span class="brand-dot"></span>Corvanel LLC</div>
  <div class="site">www.<span class="site-name">corvanel</span>.com</div>
</section>

<section class="card card--front" aria-label="Card front">
  <svg class="card-shape" viewBox="0 0 560 320" aria-hidden="true">
    <path d="M0 86 H196 L212 174 H560 V320 H0 Z" fill="var(--card-dark)"/>
    <path d="M196 86 L212 174 H560 V168 H217 L202 84 Z" fill="var(--accent)"/>
  </svg>
  <div class="brand"><span class="brand-dot"></span>Corvanel LLC</div>
  <div class="person">
    <div class="person-name">MAREN HOLLOWAY</div>
    <div class="person-role">General Manager</div>
  </div>
  <ul class="contacts">
    <li class="contact">123 4567 8900
      <svg viewBox="0 0 16 16" fill="none" stroke="#fff" stroke-width="1.6"><rect x="4" y="1" width="8" height="14" rx="1.5"/><line x1="7" y1="12.5" x2="9" y2="12.5"/></svg>
    </li>
    <li class="contact">123 4567 8900
      <svg viewBox="0 0 16 16" fill="#fff"><path d="M4 1 L6.5 4 L5 6 C6 8.5 7.5 10 10 11 L12 9.5 L15 12 L13 15 C7 14.5 1.5 9 1 3 Z"/></svg>
    </li>
    <li class="contact">48 Harbor Street, New York, USA
      <svg viewBox="0 0 16 16" fill="#fff"><path d="M8 1 C4.7 1 3 3.3 3 6 C3 9.5 8 15 8 15 C8 15 13 9.5 13 6 C13 3.3 11.3 1 8 1 Z M8 4 A2 2 0 1 1 8 8 A2 2 0 1 1 8 4 Z" fill-rule="evenodd"/></svg>
    </li>
    <li class="contact">hello@corvanel.com
      <svg viewBox="0 0 16 16" fill="none" stroke="#fff" stroke-width="1.5"><rect x="1" y="3.5" width="14" height="9" fill="#fff"/><path d="M1 3.5 L8 9 L15 3.5" stroke="var(--card-dark)"/></svg>
    </li>
    <li class="contact">www.corvanel.com
      <svg viewBox="0 0 16 16" fill="none" stroke="#fff" stroke-width="1.2"><circle cx="8" cy="8" r="6.5"/><ellipse cx="8" cy="8" rx="3" ry="6.5"/><line x1="1.5" y1="8" x2="14.5" y2="8"/><line x1="2.5" y1="4.8" x2="13.5" y2="4.8"/><line x1="2.5" y1="11.2" x2="13.5" y2="11.2"/></svg>
    </li>
  </ul>
</section>

</body>
</html>
```